The Book Cover for "Finding the Silver Lantern of Dawn" needs redesigned

First the back ground or art work needs to be replaced or redesigned.
The title Finding the Silver Lantern of Dawn needs to be redesigned so that the words "Finding the" is diminished in size compared to the rest of the title "Silver Lantern of Dawn"
The Sub-title "Tracing the forgotten path of the Evening Wind" needs to be more pronounced and readable.
The authors name needs to be downsized.

```html
<!DOCTYPE html>
<html lang="en">
<head>
<meta charset="utf-8">
<title>Finding the Silver Lantern of Dawn — Book Cover</title>
<link rel="stylesheet" href="https://fonts.googleapis.com/css2?family=Montserrat:ital,wght@0,800;0,900;1,900&display=swap">
<style>
  :root {
    --navy: #272361;
    --teal: #0db6ae;
    --ink: #111111;
    --paper: #ffffff;
    --mist: #e9edf0;
    --frame: #8a8f94;
  }
  html, body {
    margin: 0;
    padding: 0;
    width: 1200px;
    height: 1200px;
    overflow: hidden;
    background: var(--paper);
  }
  .cover {
    display: block;
    width: 1200px;
    height: 1200px;
    font-family: "Montserrat", Arial, sans-serif;
  }
  .kicker { fill: var(--navy); font-weight: 900; }
  .headline { fill: var(--teal); font-weight: 900; }
  .headline-final { fill: var(--navy); font-weight: 900; }
  .connector { fill: var(--ink); font-weight: 900; font-style: italic; }
  .subtitle { fill: var(--ink); font-weight: 800; }
  .author-band { fill: var(--teal); }
  .author-name { fill: var(--paper); font-weight: 800; letter-spacing: 9px; }
  .cover-edge { fill: none; stroke: var(--frame); stroke-width: 1; }
</style>
</head>
<body>
<svg class="cover" viewBox="0 0 1200 1200" xmlns="http://www.w3.org/2000/svg" aria-label="Book cover: Finding the Silver Lantern of Dawn">
  <defs>
    <linearGradient id="paperWash" x1="0" y1="0" x2="1" y2="0">
      <stop offset="0" stop-color="#ffffff"/>
      <stop offset="0.5" stop-color="#f3f5f7"/>
      <stop offset="1" stop-color="#e6eaee"/>
    </linearGradient>
    <linearGradient id="sceneTones" x1="0" y1="0" x2="0.6" y2="1">
      <stop offset="0" stop-color="#f4f6f8" stop-opacity="0"/>
      <stop offset="0.25" stop-color="#e9d5c6" stop-opacity="0.55"/>
      <stop offset="0.55" stop-color="#c99a7e" stop-opacity="0.7"/>
      <stop offset="0.8" stop-color="#3f7fcf" stop-opacity="0.75"/>
      <stop offset="1" stop-color="#eef1f4" stop-opacity="0.9"/>
    </linearGradient>
  </defs>

  <rect class="cover-paper" x="266" y="41" width="757" height="1134" fill="url(#paperWash)"/>

  <rect class="cover-artwork" x="266" y="688" width="757" height="437" fill="url(#sceneTones)"
        role="img" aria-label="Warm photograph of a smiling mother holding her laughing baby in a bright room"/>

  <text class="kicker" x="369" y="153" font-size="71" textLength="553" lengthAdjust="spacingAndGlyphs">FINDING THE</text>
  <text class="headline" x="361" y="281" font-size="163" textLength="575" lengthAdjust="spacingAndGlyphs">SILVER</text>
  <text class="headline" x="364" y="442" font-size="217" textLength="567" lengthAdjust="spacingAndGlyphs">LANTERN</text>
  <text class="connector" x="361" y="531" font-size="71" textLength="86" lengthAdjust="spacingAndGlyphs">OF</text>
  <text class="headline-final" x="453" y="597" font-size="218" textLength="463" lengthAdjust="spacingAndGlyphs">DAWN</text>

  <text class="subtitle" x="362" y="644" font-size="29" textLength="540" lengthAdjust="spacingAndGlyphs">TRACING THE FORGOTTEN PATH OF</text>
  <text class="subtitle" x="637" y="678" font-size="29" text-anchor="middle">THE EVENING WIND</text>

  <rect class="author-band" x="266" y="1125" width="757" height="50"/>
  <text class="author-name" x="644" y="1158" font-size="23" text-anchor="middle">R. L. MARLOW ASHCOMBE</text>

  <rect class="cover-edge" x="266" y="41" width="757" height="1134"/>
</svg>
</body>
</html>
```